brochure for high-end senior living company

We need a new brochure that we can pass out to doctors and social workers so they would choose us over the competition.
brightmeadowhaven.example is our website that shows our colors and themes

we stand out over our competition due to our high quality of staff and our staff to resident ratio.
We are not afraid of difficult and complex care situations. Instead, we thrive on coordinating complexity.

We do all of this in a lovely setting that is luxurious and feels like home.

Target Market(s)

The families who make the decision are 60-70 years old. They are not not "rich" but they have saved well and usually have more than 1 million in assets.

Industry/Entity Type

Senior Living, Memory Care

Font styles to use
Serif

Colors
00AB8E
00BBA5
67D7C9
C6EFE9
E9F9F6
FFC000
F8CF3A
FAE287
FDF2CF
FEFAEE

Requirements
Must have
• When compromise is not an option...
Nice to have
• A difficult balance of beautiful and activities (happy people), but also communicating that we handle difficult and complex care.

```html
<!DOCTYPE html>
<html lang="en">
<head>
<meta charset="utf-8">
<title>Bright Meadow Residential Assisted Living – Brochure</title>
<link rel="stylesheet" href="https://fonts.googleapis.com/css2?family=Cinzel:wght@400;500&family=Cormorant+Garamond:ital,wght@0,500;1,500&family=Poppins:wght@300;400;500&display=swap">
<style>
:root{
  --backdrop:#5f5f5f;
  --teal:#00AB8E;
  --teal-bright:#00BBA5;
  --teal-ink:#007a66;
  --mint:#C6EFE9;
  --gold:#d4ae3c;
  --gold-light:#FAE287;
  --cream:#FDF2CF;
  --paper:#ffffff;
  --ink:#3a3a3a;
}
*{box-sizing:border-box;margin:0;padding:0}
html,body{width:832px;height:1200px;overflow:hidden}
body{background:var(--backdrop);font-family:"Poppins",sans-serif;color:var(--ink);position:relative}
.spread{position:absolute;left:90px;width:640px;height:496px;display:flex;box-shadow:0 6px 14px rgba(0,0,0,.35);overflow:hidden}
.spread--outside{top:83px}
.spread--inside{top:618px}
.panel{position:relative;width:213.33px;height:100%;overflow:hidden}
.photo{position:absolute;display:block}
.serif-head{font-family:"Cinzel",serif;font-weight:400;letter-spacing:.3px}
.body-copy{font-size:6.6px;line-height:9.4px;text-align:justify;font-weight:300}
.body-copy p{margin-bottom:9px}

/* about */
.about{background:var(--paper);padding:20px 14px 0 14px}
.about h2{font-size:12.5px;color:var(--teal-ink);padding-bottom:4px;border-bottom:1.5px solid var(--gold);width:108px;margin-bottom:12px}
.about .sub{font-size:7.4px;color:var(--teal-ink);font-weight:500;margin-bottom:7px}
.about .lead{font-weight:500;color:var(--teal-ink)}
.about .photo{left:0;bottom:0;width:100%;height:155px;background:linear-gradient(160deg,#e8e2d0,#a9a48c 45%,#6d7155)}

/* contact */
.contact{background:var(--teal)}
.contact .lower{position:absolute;left:0;bottom:16px;width:100%;height:140px;background:var(--gold)}
.contact .wordmark{position:absolute;top:28px;width:100%;text-align:center;color:#fff}
.wordmark-name{font-family:"Cinzel",serif;font-weight:500;font-size:19px;display:block}
.wordmark-tag{font-family:"Cormorant Garamond",serif;font-weight:500;font-size:10.5px;display:block;margin-top:2px}
.contact .wordmark::after{content:"";display:block;width:150px;height:1px;background:var(--gold-light);margin:4px auto 0}
.contact .house{left:15px;top:78px;width:182px;height:106px;border:2px solid var(--gold-light);border-radius:6px;background:linear-gradient(180deg,#9fc3e0,#d9d2bf 55%,#7a8b56)}
.contact .address{position:absolute;top:195px;width:100%;text-align:center;color:#fff;font-size:8.2px;line-height:1.3}
.contact .call{position:absolute;top:222px;width:100%;text-align:center;color:#fff;font-size:15px}
.contact .phone-pill{position:absolute;top:252px;left:40px;width:136px;height:19px;border-radius:10px;background:var(--gold);color:#fff;font-size:13px;display:flex;align-items:center;justify-content:center;gap:5px}
.contact .social{position:absolute;top:283px;width:100%;display:flex;justify-content:center;gap:7px}
.contact .social span{width:12px;height:12px;border:1px solid #fff;border-radius:50%}
.circ{position:absolute;border-radius:50%;border:3px solid var(--gold-light)}
.contact .c1{left:12px;top:318px;width:68px;height:68px;background:radial-gradient(circle at 40% 40%,#d6c7b2,#6f5e4a)}
.contact .c3{left:140px;top:318px;width:68px;height:68px;background:radial-gradient(circle at 50% 40%,#c9b7a6,#5c5042)}
.contact .c2{left:64px;top:304px;width:86px;height:86px;background:radial-gradient(circle at 50% 40%,#e7dccd,#7b6a55);z-index:2}
.contact .info{position:absolute;top:415px;width:100%;text-align:center;color:var(--teal-ink)}
.contact .info .name{font-family:"Cinzel",serif;font-size:8.8px;font-weight:500;line-height:1.25}
.contact .info .line{font-size:9.4px;line-height:1.3}
.band{position:absolute;bottom:0;left:0;width:100%;height:16px;background:var(--teal);color:#fff;font-size:9.4px;display:flex;align-items:center;justify-content:center}
.band b{font-weight:500}

/* cover */
.cover{background:var(--paper)}
.cover .wordmark{position:absolute;top:24px;width:100%;text-align:center;color:var(--teal-ink)}
.cover .wordmark-name{font-size:23px}
.cover .wordmark-tag{font-size:13px;color:#222;margin-top:4px}
.cover .rule{position:absolute;top:28px;left:24px;width:166px;height:1px;background:var(--gold)}
.cover .photo{left:0;top:98px;width:100%;height:300px;background:linear-gradient(150deg,#e3d28a,#9aa45a 35%,#3f5a2c 70%,#6d6a3c)}
.cover .lower{position:absolute;left:0;bottom:16px;width:100%;height:98px;background:var(--gold)}
.cover .promise{position:absolute;top:395px;width:100%;text-align:center;color:var(--teal-ink);font-family:"Cormorant Garamond",serif;font-style:italic;font-weight:500;font-size:11px}
.cover .tagline{position:absolute;top:412px;width:100%;text-align:center;color:#fff;font-size:14.5px;line-height:1.2}
.cover .tagline small{display:block;font-family:"Poppins",sans-serif;font-size:8.3px;font-weight:500;line-height:1.05;margin-top:3px;letter-spacing:0}

/* inside */
.facility{background:var(--gold);padding:16px 13px 0 13px;color:#fff}
.facility h2{font-size:11.5px;color:var(--teal-ink);margin-bottom:14px}
.facility .sub{font-size:7.6px;color:var(--teal-ink);font-weight:500;margin-bottom:7px}
.facility .body-copy{line-height:9.6px}
.facility .body-copy p{margin-bottom:10px}
.facility .photo{left:0;bottom:0;width:100%;height:150px;background:linear-gradient(170deg,#c9d8e6,#8fa874 40%,#6b6f54 75%,#3d3d44)}

.services{background:linear-gradient(180deg,#fff,#eef5f3);padding:16px 13px 0 13px}
.services h2{font-size:11.5px;color:var(--teal-ink);text-align:center;margin-bottom:14px}
.services .body-copy p{margin-bottom:8px}
.gallery{position:absolute;top:155px;left:10px;width:193px;display:grid;grid-template-columns:1fr 1fr;gap:3px}
.gallery div{height:73px;border:1.5px solid var(--gold-light)}
.g1{background:linear-gradient(160deg,#e2cfa6,#a57d4b)}
.g2{background:linear-gradient(160deg,#eef0ee,#7f8b78)}
.g3{background:linear-gradient(160deg,#f0ece6,#8e5a3a)}
.g4{background:linear-gradient(170deg,#a9c4de,#7e8a6a 55%,#c7a98b)}
.services h3{position:absolute;top:322px;width:100%;left:0;text-align:center;font-size:9.4px;font-weight:400;color:var(--teal-ink);line-height:1.5}
.care-list{position:absolute;top:354px;left:18px;list-style:none}
.care-list li{font-size:8.2px;line-height:15.3px;display:flex;align-items:center;gap:5px}
.care-list svg{width:8px;height:8px}

.reasons{background:var(--gold)}
.reasons .photo{left:0;top:0;width:100%;height:180px;background:linear-gradient(170deg,#dfe2d9,#8b7a60 45%,#5b4638)}
.reasons .wave{position:absolute;top:160px;left:0}
.reasons .c4{left:130px;top:140px;width:78px;height:78px;background:radial-gradient(circle at 50% 40%,#f1e7dc,#a37f6a);z-index:2}
.reasons h2{position:absolute;top:220px;left:10px;font-size:11.5px;color:var(--teal-ink)}
.reasons .lead{position:absolute;top:245px;left:10px;width:190px;font-size:6.6px;color:#fff;line-height:9.4px;font-weight:300}
.perks{position:absolute;top:290px;left:10px;list-style:none}
.perks li{display:flex;align-items:center;gap:5px;color:#fff;font-size:8.3px;line-height:1;min-height:24px}
.perks .ico{width:18px;height:18px;border-radius:50%;background:#fff;flex:none;display:flex;align-items:center;justify-content:center}
.perks .ico span{width:10px;height:10px;border-radius:50%;background:var(--teal)}
.quote{position:absolute;top:400px;left:8px;width:197px;height:65px;border:1px solid #fff;border-radius:5px;color:#fff;font-size:6.2px;font-style:italic;font-weight:300;line-height:1.5;padding:12px 5px 0 6px}
.quote .mark{position:absolute;top:-12px;left:85px;width:26px;background:var(--gold);text-align:center;font-family:"Cormorant Garamond",serif;font-size:26px;font-style:normal;line-height:22px}
.inside-band{position:absolute;bottom:0;left:213.33px;width:426.67px;height:16px;background:var(--teal);color:#fff;font-size:7px;display:flex;align-items:center;justify-content:center;z-index:3}
</style>
</head>
<body>

<section class="spread spread--outside">
  <article class="panel about">
    <h2 class="serif-head">About Us</h2>
    <p class="sub">Quality of Life You Want for Your Loved Ones</p>
    <div class="body-copy">
      <p>At Bright Meadow Residential Assisted Living, our team of highly trained and caring professionals provides a welcoming and comfortable assisted living environment for our residents to enjoy for many years to come.</p>
      <p>Unlike other communities, our Maplecrest assisted living home is located in a residential setting because we believe it brings a greater value to our residents as they maintain feelings of safety, warmth, and familiarity.</p>
      <p>The most beneficial factor of living in our community is the great amount of personal care and attention we are able to give each one of our residents. In fact, we maintain the highest caregiver to resident ratio in the assisted living industry. More than anything, we believe</p>
      <p>Bright Meadow Residential Assisted Living is the trusted solution for families who put quality care as their highest priority.</p>
      <p class="lead">If you are seeking assisted living in Cedar Hollow or Maplecrest, you can feel confident turning to all Bright Meadow Residential Assisted Living!</p>
    </div>
    <svg width="214" height="40" style="position:absolute;left:0;top:320px;z-index:2" viewBox="0 0 214 40"><path d="M0 30 Q110 -5 214 8 L214 0 L0 0Z" fill="#fff"/><path d="M0 30 Q110 -5 214 8" stroke="#FAE287" stroke-width="4" fill="none"/></svg>
    <div class="photo" role="img" aria-label="Residents dining together on a shaded patio under a large umbrella"></div>
  </article>

  <article class="panel contact">
    <div class="lower"></div>
    <div class="wordmark">
      <span class="wordmark-name">Bright Meadow</span>
      <span class="wordmark-tag">Residential Assisted Living</span>
    </div>
    <div class="photo house" role="img" aria-label="Single-storey residential care home with a tiled roof and front lawn"></div>
    <p class="address">4120 Linden Way<br>Maplecrest, CA 90000</p>
    <p class="call serif-head">Call Us Today:</p>
    <div class="phone-pill">
      <svg width="11" height="11" viewBox="0 0 24 24"><circle cx="12" cy="12" r="10.5" fill="none" stroke="#fff" stroke-width="2"/><path d="M8.5 6.5l2 2-1.2 1.6a8 8 0 0 0 4.6 4.6l1.6-1.2 2 2-1.4 1.6c-4.5-.5-8.7-4.7-9.2-9.2z" fill="#fff"/></svg>
      555-014-2870
    </div>
    <div class="social" aria-label="Social media"><span></span><span></span><span></span></div>
    <div class="circ c1 photo" role="img" aria-label="Resident playing piano"></div>
    <div class="circ c2 photo" role="img" aria-label="Musician playing the harp for residents"></div>
    <div class="circ c3 photo" role="img" aria-label="Smiling residents at a group activity"></div>
    <div class="info">
      <p class="name">Bright Meadow<br>Residential Assisted Living</p>
      <p class="line">555-014-2870</p>
      <p class="line">admin@brightmeadowhaven.example</p>
    </div>
    <div class="band">www.<b>brightmeadowhaven</b>.example</div>
  </article>

  <article class="panel cover">
    <div class="rule"></div>
    <div class="wordmark">
      <span class="wordmark-name">Bright Meadow</span>
      <span class="wordmark-tag">Residential Assisted Living</span>
    </div>
    <div class="photo" role="img" aria-label="Caregiver pushing a smiling senior man in a wheelchair outdoors in sunlit trees"></div>
    <svg width="214" height="30" style="position:absolute;left:0;top:90px" viewBox="0 0 214 30"><path d="M0 0 L214 0 L214 8 Q110 22 0 4Z" fill="#fff"/><path d="M0 4 Q110 22 214 8" stroke="#FAE287" stroke-width="3" fill="none"/></svg>
    <svg width="214" height="40" style="position:absolute;left:0;top:362px" viewBox="0 0 214 40"><path d="M0 40 L0 22 Q100 -6 214 18 L214 40Z" fill="#d4ae3c"/><path d="M0 22 Q100 -6 214 18" stroke="#FDF2CF" stroke-width="4" fill="none"/></svg>
    <div class="lower"></div>
    <p class="promise">When compromise is not an option...</p>
    <p class="tagline serif-head">The Perfect Balance of<br>Safety &amp; Warmth<small>Professional &amp; Friendly Care in a<br>Home Environment</small></p>
    <div class="band">www.<b>brightmeadowhaven</b>.example</div>
  </article>
</section>

<section class="spread spread--inside">
  <article class="panel facility">
    <h2 class="serif-head">Assisted Living Facility</h2>
    <p class="sub">We'll Treat Your Loved One Like Family</p>
    <div class="body-copy">
      <p>We at Bright Meadow Residential Assisted Living realize that entrusting the health and well-being of your elderly loved one to an assisted living home is no easy decision.</p>
      <p>You want to find a home that will provide them with exceptional care in a beautiful and pleasant setting. Most assisted living homes look and feel institutional and sterile - but not ours.</p>
      <p>Our assisted living home looks like the other homes that line our residential street. We opened our doors with the purpose of providing the best combination of professional care and a comfortable home environment for seniors in Maplecrest. If you are seeking assisted living in Cedar Hollow or Maplecrest, you can feel confident turning to all Bright Meadow Residential Assisted Living!</p>
      <p>Our family-focused assisted living home welcomes you to seek more information about our caring and professional services. Let us help you take care of your loved one. At Bright Meadow, your loved one will be treated like family. Please contact us to learn more about how we can help you and your loved one make the transition into assisted care.</p>
    </div>
    <svg width="214" height="30" style="position:absolute;left:0;top:336px;z-index:2" viewBox="0 0 214 30"><path d="M0 0 L214 0 L214 14 Q100 -4 0 18Z" fill="#d4ae3c"/><path d="M0 18 Q100 -4 214 14" stroke="#FDF2CF" stroke-width="4" fill="none"/></svg>
    <div class="photo" role="img" aria-label="Three residents sharing a meal at a patio table under an umbrella"></div>
  </article>

  <article class="panel services">
    <h2 class="serif-head">Services We Provide</h2>
    <div class="body-copy">
      <p>You want to find a home that will provide them with exceptional care in a beautiful and pleasant setting. Most assisted living homes look and feel institutional and sterile - but not ours.</p>
      <p>Our assisted living home looks like the other homes that line our residential street. We opened our doors with the purpose of providing the best combination of professional care and a comfortable home environment for seniors in Maplecrest.</p>
    </div>
    <div class="gallery">
      <div class="g1" role="img" aria-label="Warm living room with armchairs and a coffee table"></div>
      <div class="g2" role="img" aria-label="Bright private bedroom with an armchair"></div>
      <div class="g3" role="img" aria-label="Cosy lounge with a fireplace and leather seating"></div>
      <div class="g4" role="img" aria-label="Garden patio with umbrellas and outdoor furniture"></div>
    </div>
    <h3>Around the Clock Quality Care for<br>Your Loved One.</h3>
    <ul class="care-list">
      <li><svg viewBox="0 0 10 10"><circle cx="5" cy="5" r="4.3" fill="none" stroke="#007a66"/><path d="M4 3l2 2-2 2" fill="none" stroke="#007a66"/></svg>Alzheimer's &amp; Dementia Care</li>
      <li><svg viewBox="0 0 10 10"><circle cx="5" cy="5" r="4.3" fill="none" stroke="#007a66"/><path d="M4 3l2 2-2 2" fill="none" stroke="#007a66"/></svg>Stroke Care</li>
      <li><svg viewBox="0 0 10 10"><circle cx="5" cy="5" r="4.3" fill="none" stroke="#007a66"/><path d="M4 3l2 2-2 2" fill="none" stroke="#007a66"/></svg>Parkinson's Care</li>
      <li><svg viewBox="0 0 10 10"><circle cx="5" cy="5" r="4.3" fill="none" stroke="#007a66"/><path d="M4 3l2 2-2 2" fill="none" stroke="#007a66"/></svg>Limited Mobility</li>
      <li><svg viewBox="0 0 10 10"><circle cx="5" cy="5" r="4.3" fill="none" stroke="#007a66"/><path d="M4 3l2 2-2 2" fill="none" stroke="#007a66"/></svg>Hospice Care</li>
      <li><svg viewBox="0 0 10 10"><circle cx="5" cy="5" r="4.3" fill="none" stroke="#007a66"/><path d="M4 3l2 2-2 2" fill="none" stroke="#007a66"/></svg>Skin &amp; Incontinence Care</li>
      <li><svg viewBox="0 0 10 10"><circle cx="5" cy="5" r="4.3" fill="none" stroke="#007a66"/><path d="M4 3l2 2-2 2" fill="none" stroke="#007a66"/></svg>Short Term Stays</li>
    </ul>
  </article>

  <article class="panel reasons">
    <div class="photo" role="img" aria-label="Residents painting at easels in a sunny activity room"></div>
    <svg class="wave" width="214" height="40" viewBox="0 0 214 40"><path d="M0 40 L0 22 Q100 -4 214 20 L214 40Z" fill="#d4ae3c"/><path d="M0 22 Q100 -4 214 20" stroke="#FDF2CF" stroke-width="4" fill="none"/></svg>
    <div class="circ c4 photo" role="img" aria-label="Residents enjoying an ice cream truck visit outdoors"></div>
    <h2 class="serif-head">Reasons to Choose Us</h2>
    <p class="lead">We at Bright Meadow Residential Assisted Living realize that entrusting the health and well-being of your elderly loved one to an assisted living home is no easy decision.</p>
    <ul class="perks">
      <li><span class="ico"><span></span></span>Private Rooms and Bathrooms</li>
      <li><span class="ico"><span></span></span>Delicious and Healthy Home<br>Cooked Meals</li>
      <li><span class="ico"><span></span></span>Highest Caregiver to Resident<br>Ratio in the Industry</li>
      <li><span class="ico"><span></span></span>24/7 Well-Trained Caregivers on Site</li>
    </ul>
    <blockquote class="quote"><span class="mark">&ldquo;</span>Bright Meadow provided my husband with professional, loving care in his last years of life. He had been in a larger memory care facility essentially locked up with no access to the outdoors without ..."<br>- Dana Whitfield</blockquote>
  </article>

  <div class="inside-band">Interested In Our Care &amp; Services? Call (555) 014-2870 Today To Request A Free Consultation &amp; Community Tour</div>
</section>

</body>
</html>
```